Stationery & Envelope Design

Executive Style looking stationery & envelope design.
Business Information:
Halvern Crest Properties
2875 Birchwood Lane, Roseville, CA 95712-4408
Phone: 916.555.0142
Fax: 916.555.0187

Industry/Entity Type

Business

```html
<!DOCTYPE html>
<html lang="en">
<head>
<meta charset="UTF-8">
<title>Halvern Crest Properties — Envelope</title>
<link href="https://fonts.googleapis.com/css2?family=Fira+Sans:wght@400&family=Fira+Sans+Condensed:wght@600&display=swap" rel="stylesheet">
<style>
  :root {
    --paper: #ffffff;
    --ink: #1a1a1a;
    --brand-navy: #0f2a8c;
    --green-light: #8cc63f;
    --green-dark: #2f5a1f;
    --band-navy: #0a1a6e;
    --band-bright: #1d3cff;
    --mark-grey: #e2e2e2;
    --mark-grey-soft: #efefef;
  }
  html, body {
    margin: 0;
    padding: 0;
    overflow: hidden;
    background: var(--paper);
  }
  .envelope {
    position: relative;
    width: 1200px;
    height: 960px;
    background: var(--paper);
    overflow: hidden;
  }
  .return-address {
    position: absolute;
    left: 128px;
    top: 274px;
    font-family: "Fira Sans", Arial, sans-serif;
    font-style: normal;
    font-size: 19px;
    line-height: 23px;
    color: var(--ink);
  }
  .company-name {
    margin: 0 0 2px;
    font-family: "Fira Sans Condensed", "Arial Narrow", sans-serif;
    font-weight: 600;
    font-size: 27px;
    line-height: 30px;
    color: var(--brand-navy);
    text-transform: uppercase;
    letter-spacing: 0.2px;
  }
  .street, .contact {
    margin: 0;
  }
  .contact {
    margin-top: 28px;
  }
  .brand-watermark {
    position: absolute;
    left: 116px;
    top: 496px;
    width: 386px;
    height: 204px;
    border-radius: 6px;
    background: linear-gradient(160deg, var(--mark-grey) 0%, var(--mark-grey-soft) 100%);
    opacity: 0.6;
  }
  .accent-rule {
    position: absolute;
    left: 109px;
    top: 703px;
    width: 1009px;
    height: 6px;
    background: linear-gradient(90deg, var(--green-light) 0%, var(--green-dark) 100%);
  }
  .base-band {
    position: absolute;
    left: 109px;
    top: 714px;
    width: 1009px;
    height: 36px;
    background: linear-gradient(90deg, var(--band-navy) 0%, var(--band-bright) 100%);
  }
</style>
</head>
<body>
  <main class="envelope">
    <address class="return-address">
      <p class="company-name">Halvern Crest Properties</p>
      <p class="street">2875 Birchwood Lane<br>Ashford, CA 95712-4408</p>
      <p class="contact">P: 916.555.0142<br>F: 916.555.0187</p>
    </address>
    <div class="brand-watermark" role="img" aria-label="Faint grey brand artwork area behind the return address"></div>
    <div class="accent-rule"></div>
    <div class="base-band"></div>
  </main>
</body>
</html>
```